Corvella Website Homepage

Committed to delivering quality content, quillpagewords.com is a content providing company. Equipped with resourceful writers with industry experience, we promise to empower our clients with content that is tailor-made to address specific requirements of their target Audience.

We need a website home page and one internal page designed. It is very important that the page be laid out with SEO in mind. We like the idea of using five images as navigation to our services. The five major services we offer are:
• Web Content writing (articles, features, website copy etc)
• Business Content writing (Press release, mailers & flyers, brochure/catalog)
• Personal Content writing (blog, speech writing)
• Hire a writer/editor
• Proof reading and editing services
The sample template (http://pv7.layoutdemo-hub.net/dx_48270/index.html) included has five images in the first fold. Designer can choose the right image for each service and lay over the service name on the image. Please do not use flash ( We will use javascripts). We need to have a detailed right side nav as in the template for SEO reasons. There will be some marketing ad- copy below the main images. Followed by a 200 character SEO optimized text defining our services in further detail. Apart from these a designer is free to use his creativity. The name of the site will be http://www.quillpagewords.com/. This name will need a logo too. Please include it as part of design. Corvellacorp is the owner of quillpagewords.com. We already have a logo for Corvella that is attached here as a separate file.

We have some taglines that need to be incorporated in the home page and other pages.
Please provide link button for Home, About us, Services, Samples, Pricing, Clients, Career, Contact us.

Links can be given on TOP, Sideways and Bottom and in the drop down menu of services etc.

Reason: Hi

We have made our project guaranteed and extended deadline by 5 days so you get more time to complete our project.

Thanks and Regards,

Ravindra Kulkarni
Corvellacorp

Target Market(s)

Product Marketing Companies - Mostly in US.
Media companies which publish articles on various subjects. Travel and Lifestyle related sites, Educational Websites, Government Websites, Health related websites,

Industry/Entity Type

Marketing

Requirements
Must have
• Color of Homepage should blend with sober mood of the content. Writing Services should get highlighted in such a way that any person serious about the business visiting the site get attracted to read on the details of our content services. Most space should be used for details of writing services and links for our various pages and services. Webpage should be downloaded in lowest possible time.
Nice to have
• We have some idea about the website layouts;-http://www.skinbazaarly.net/site-layouts/48270.html - layout of information http://www.skinbazaarly.net/site-layouts/47359.html - for kind of marketing http://pv7.layoutdemo-hub.net/dx_48615/index.html - for colors
we attach a word file representing our idea in some way but not limited to it.
Should not have
• Gaudy (aggressive dark) colors. It should not be cluttered. No flash.

```html
<!DOCTYPE html>
<html lang="en">
<head>
<meta charset="utf-8">
<title>quillpagewords.com — Content Writing Services</title>
<link rel="stylesheet" href="https://fonts.googleapis.com/css2?family=Arimo:wght@400;700&display=swap">
<style>
  :root {
    --red: #e3141b;
    --orange: #f26a1b;
    --ink: #222222;
    --text: #4a4a4a;
    --rule: #bdbdbd;
    --dot: #cfcfcf;
    --panel-border: #c9c9c9;
    --footer: #3b3b3b;
    --white: #ffffff;
  }
  * { margin: 0; padding: 0; box-sizing: border-box; }
  html, body { width: 891px; height: 1200px; overflow: hidden; background: var(--white); }
  body { position: relative; font-family: "Arimo", Arial, sans-serif; color: var(--text); }
  a { color: inherit; text-decoration: none; }
  .abs { position: absolute; }

  /* Brand (plain wordmark) */
  .brand-name { display: block; font-weight: 700; color: #3a3a3a; letter-spacing: -1px; line-height: 0.9; white-space: nowrap; }
  .site-brand { left: 82px; top: 33px; }
  .site-brand .brand-name { font-size: 25px; }

  /* Header tools */
  .languages { left: 531px; top: 33px; display: flex; gap: 8px; }
  .lang { width: 21px; height: 21px; border-radius: 2px; }
  .lang-en { background: #3a4b8c; }
  .lang-de { background: linear-gradient(#222 0 33%, #d21c1c 33% 66%, #f2c200 66%); }
  .lang-es { background: linear-gradient(#c8161d 0 25%, #f4c300 25% 75%, #c8161d 75%); }
  .search { left: 628px; top: 30px; width: 158px; height: 24px; border-radius: 12px; background: linear-gradient(#dcdcdc, #efefef); }
  .search svg { position: absolute; right: 8px; top: 4px; }
  .mascot { left: 800px; top: 18px; width: 52px; height: 60px; border-radius: 26px 26px 20px 20px; background: radial-gradient(circle at 40% 35%, #5bb8f0, #1d7fc4); }

  /* Main nav */
  .main-nav { left: 26px; top: 104px; width: 834px; display: flex; gap: 2px; }
  .main-nav a { flex: 1; text-align: center; font-size: 12.5px; letter-spacing: -0.3px; color: #333; padding-bottom: 8px; border-bottom: 2px solid var(--rule); text-transform: uppercase; white-space: nowrap; }
  .main-nav a.active { color: var(--red); font-weight: 700; border-bottom: 4px solid var(--red); padding-bottom: 6px; }

  /* Service strip */
  .services { left: 23px; top: 150px; width: 837px; height: 294px; display: flex; }
  .service { position: relative; flex: 1; overflow: hidden; }
  .service-1 { background: radial-gradient(ellipse at 35% 55%, #f4f4f4 0%, #cfcfcf 45%, #8e8e8e 100%); }
  .service-2 { background: radial-gradient(ellipse at 55% 30%, #efefef 0%, #b9b9b9 40%, #2e2e2e 100%); }
  .service-3 { background: radial-gradient(ellipse at 45% 50%, #9a9a9a 0%, #6a6a6a 45%, #3c3c3c 100%); }
  .service-4 { background: radial-gradient(ellipse at 40% 60%, #fafafa 0%, #dcdcdc 45%, #4a4a4a 100%); }
  .service-5 { background: radial-gradient(ellipse at 60% 55%, #c4c4c4 0%, #e2e2e2 45%, #f4f4f4 100%); }
  .service-label { position: absolute; right: 8px; bottom: 14px; writing-mode: vertical-rl; transform: rotate(180deg); color: var(--white); font-weight: 700; font-size: 17px; letter-spacing: -0.4px; white-space: nowrap; text-shadow: 0 0 3px rgba(0,0,0,.35); }

  /* Promo banner */
  .promo { left: 23px; top: 467px; width: 613px; height: 339px; background: radial-gradient(ellipse at 22% 35%, var(--orange) 0%, #ee3f18 45%, var(--red) 80%); color: var(--white); }
  .promo-brand { left: 63px; top: 16px; }
  .promo-brand .brand-name { font-size: 21px; color: #4a4a4a; }
  .promo-nav { left: 199px; top: 17px; display: flex; gap: 14px; font-size: 8.5px; letter-spacing: -0.2px; text-transform: uppercase; white-space: nowrap; }
  .promo-nav a.active { font-weight: 700; }
  .headline { font-weight: 400; letter-spacing: -1.2px; line-height: 1; white-space: nowrap; }
  .headline-a { left: 84px; top: 128px; font-size: 28px; }
  .headline-b { left: 176px; top: 157px; font-size: 11px; letter-spacing: -0.3px; }
  .headline-c { left: 284px; top: 145px; font-size: 29px; }
  .headline-d { left: 466px; top: 171px; font-size: 14px; letter-spacing: -0.5px; }
  .promo-copy { left: 31px; top: 282px; width: 560px; font-size: 12.5px; line-height: 15px; }

  /* Sidebar */
  .side-nav { left: 648px; top: 465px; width: 213px; height: 246px; border: 1px solid var(--panel-border); border-radius: 7px; padding: 14px 10px 0 10px; }
  .side-title { font-size: 17px; color: var(--red); font-weight: 400; margin-bottom: 7px; }
  .side-nav ul { list-style: none; }
  .side-nav li { height: 22.8px; border-bottom: 1px dotted var(--dot); display: flex; align-items: center; font-size: 11px; color: #555; }
  .side-nav li:last-child { border-bottom: none; }
  .chev { width: 14px; margin-right: 8px; flex: none; }
  .newsletter-title { left: 648px; top: 722px; font-size: 15px; font-weight: 700; color: var(--ink); }
  .email { left: 648px; top: 743px; width: 214px; height: 25px; border: 1px solid #bbb; font-size: 13px; color: #c5c5c5; padding: 4px 6px; }
  .unsubscribe { left: 652px; top: 783px; display: flex; align-items: center; font-size: 11px; color: #444; }
  .unsubscribe .chev { margin-right: 2px; }
  .btn-red { background: linear-gradient(#f7721f, #e3301a); color: var(--white); font-weight: 700; font-size: 12px; text-align: center; border-radius: 2px; }
  .newsletter-submit { left: 785px; top: 776px; width: 78px; height: 22px; line-height: 22px; }

  /* Content columns */
  .column { top: 838px; width: 279px; height: 230px; border-top: 1px dotted var(--dot); border-bottom: 1px dotted var(--dot); padding-top: 10px; }
  .col-prices { left: 26px; }
  .col-work { left: 355px; }
  .column h2 { font-weight: 400; font-size: 21px; color: var(--ink); letter-spacing: -0.6px; line-height: 24px; margin-bottom: 2px; }
  .column p { font-size: 9px; letter-spacing: -0.15px; line-height: 14px; color: #555; margin-bottom: 14px; }
  .column p b { color: #333; }
  .read-more { position: absolute; right: 5px; bottom: 14px; width: 63px; height: 18px; line-height: 18px; background: linear-gradient(#4a4a4a, #111); color: var(--white); font-size: 10px; text-align: center; border-radius: 2px; }

  .follow { left: 648px; top: 840px; width: 213px; height: 82px; border: 1px solid var(--panel-border); border-radius: 4px; padding: 9px 8px; }
  .follow-title { display: flex; align-items: center; font-size: 11px; color: #333; }
  .follow-title .chev { width: 10px; margin-right: 6px; }
  .social { display: flex; gap: 6px; margin: 15px 0 0 17px; }
  .social span { width: 22px; height: 22px; border-radius: 3px; }
  .social .s1 { background: linear-gradient(#f2f2f2, #d6d6d6); }
  .social .s2 { background: linear-gradient(#8a8a8a, #3c3c3c); }
  .social .s3 { background: linear-gradient(#5c7fc4, #2d4f95); }
  .social .s4 { background: linear-gradient(#8fd0ef, #3da3d6); }
  .social .s5 { background: linear-gradient(#d04a3a, #8e1f16); }
  .social .s6 { background: linear-gradient(#6fc07a, #2f8a3d); }
  .work-title { left: 648px; top: 946px; font-size: 15px; font-weight: 700; color: var(--ink); }
  .work-card { left: 648px; top: 972px; width: 214px; height: 98px; background: radial-gradient(ellipse at 70% 35%, #9a9a9a 0%, #dcdcdc 40%, #f7f7f7 100%); box-shadow: 0 1px 3px rgba(0,0,0,.25); }
  .work-submit { left: 772px; top: 1038px; width: 78px; height: 22px; line-height: 22px; }

  /* Footer */
  .footer { left: 0; top: 1128px; width: 891px; height: 72px; background: var(--footer); color: var(--white); }
  .footer-brand { left: 56px; top: 16px; }
  .footer-brand .brand-name { font-size: 13px; color: var(--white); letter-spacing: -0.5px; }
  .footer-legal { left: 58px; top: 43px; font-size: 7px; color: #ddd; }
  .footer-nav { left: 255px; top: 17px; display: flex; font-size: 9px; white-space: nowrap; }
  .footer-nav a + a::before { content: "|"; margin: 0 8px; color: #aaa; }
</style>
</head>
<body>

<header>
  <a class="abs site-brand" href="http://www.quillpagewords.com/">
    <span class="brand-name">quillpage<br>words.com</span>
  </a>
  <div class="abs languages">
    <span class="lang lang-en" role="img" aria-label="English"></span>
    <span class="lang lang-de" role="img" aria-label="German"></span>
    <span class="lang lang-es" role="img" aria-label="Spanish"></span>
  </div>
  <div class="abs search" role="search">
    <svg width="16" height="16" viewBox="0 0 16 16"><circle cx="6.5" cy="6.5" r="4.5" fill="none" stroke="#777" stroke-width="2"/><line x1="10" y1="10" x2="14.5" y2="14.5" stroke="#777" stroke-width="2.4" stroke-linecap="round"/></svg>
  </div>
  <div class="abs mascot" role="img" aria-label="Blue bird mascot illustration"></div>

  <nav class="abs main-nav">
    <a class="active" href="#">Home</a>
    <a href="#">About Us</a>
    <a href="#">Services</a>
    <a href="#">Samples</a>
    <a href="#">Pricing</a>
    <a href="#">Clients</a>
    <a href="#">Career</a>
    <a href="#">Contact Us</a>
  </nav>
</header>

<section class="abs services" aria-label="Writing services">
  <a class="service service-1" href="#" role="img" aria-label="Photo of hands typing on a laptop"><span class="service-label">Web Content Writing</span></a>
  <a class="service service-2" href="#" role="img" aria-label="Photo of business people reviewing documents"><span class="service-label">Business Content Writing</span></a>
  <a class="service service-3" href="#" role="img" aria-label="Photo of a keyboard with a Blog key"><span class="service-label">Personal Content Writing</span></a>
  <a class="service service-4" href="#" role="img" aria-label="Photo of a hand writing with a pen"><span class="service-label">Hire a writer/editor</span></a>
  <a class="service service-5" href="#" role="img" aria-label="Photo of a pencil eraser"><span class="service-label">Proof Reading and Editing Services</span></a>
</section>

<section class="abs promo">
  <div class="abs promo-brand">
    <span class="brand-name">quillpage<br>words.com</span>
  </div>
  <nav class="abs promo-nav">
    <a class="active" href="#">Home</a><a href="#">About Us</a><a href="#">Services</a><a href="#">Samples</a><a href="#">Pricing</a><a href="#">Clients</a><a href="#">Career</a><a href="#">Contact Us</a>
  </nav>
  <h1>
    <span class="abs headline headline-a">We will Create</span>
    <span class="abs headline headline-b">a highly result-driven</span>
    <span class="abs headline headline-c">Marketing Program</span>
    <span class="abs headline headline-d">for you.</span>
  </h1>
  <p class="abs promo-copy">Lorem ipsum dolor sit amet, consectetur adipiscing elit. Mauris pulvinar sollicitudin dui, eget tempor magna mollis sed. Aliquam rutrum risus et nulla ultrices in cursus dolor sagittis. Class posuere.</p>
</section>

<aside>
  <nav class="abs side-nav">
    <h3 class="side-title">WHAT WE DO</h3>
    <ul>
      <li><svg class="chev" viewBox="0 0 14 10" height="10"><path d="M1 1l4 4-4 4M7 1l4 4-4 4" fill="none" stroke="#e3141b" stroke-width="2.2"/></svg>Home</li>
      <li><svg class="chev" viewBox="0 0 14 10" height="10"><path d="M1 1l4 4-4 4M7 1l4 4-4 4" fill="none" stroke="#e3141b" stroke-width="2.2"/></svg>About Us</li>
      <li><svg class="chev" viewBox="0 0 14 10" height="10"><path d="M1 1l4 4-4 4M7 1l4 4-4 4" fill="none" stroke="#e3141b" stroke-width="2.2"/></svg>Services</li>
      <li><svg class="chev" viewBox="0 0 14 10" height="10"><path d="M1 1l4 4-4 4M7 1l4 4-4 4" fill="none" stroke="#e3141b" stroke-width="2.2"/></svg>Samples</li>
      <li><svg class="chev" viewBox="0 0 14 10" height="10"><path d="M1 1l4 4-4 4M7 1l4 4-4 4" fill="none" stroke="#e3141b" stroke-width="2.2"/></svg>Pricing</li>
      <li><svg class="chev" viewBox="0 0 14 10" height="10"><path d="M1 1l4 4-4 4M7 1l4 4-4 4" fill="none" stroke="#e3141b" stroke-width="2.2"/></svg>Clients</li>
      <li><svg class="chev" viewBox="0 0 14 10" height="10"><path d="M1 1l4 4-4 4M7 1l4 4-4 4" fill="none" stroke="#e3141b" stroke-width="2.2"/></svg>Carrer</li>
      <li><svg class="chev" viewBox="0 0 14 10" height="10"><path d="M1 1l4 4-4 4M7 1l4 4-4 4" fill="none" stroke="#e3141b" stroke-width="2.2"/></svg>Contact Us</li>
    </ul>
  </nav>

  <h3 class="abs newsletter-title">NEWSLETTER</h3>
  <div class="abs email">Your email here</div>
  <a class="abs unsubscribe" href="#"><svg class="chev" viewBox="0 0 14 10" height="9"><path d="M1 1l4 4-4 4M7 1l4 4-4 4" fill="none" stroke="#e3141b" stroke-width="2.2"/></svg>Unsuscribe</a>
  <a class="abs btn-red newsletter-submit" href="#">Submit</a>

  <div class="abs follow">
    <div class="follow-title"><svg class="chev" viewBox="0 0 14 10" height="9"><path d="M1 1l4 4-4 4M7 1l4 4-4 4" fill="none" stroke="#e3141b" stroke-width="2.2"/></svg>Follow Us</div>
    <div class="social">
      <span class="s1" role="img" aria-label="Photo sharing profile"></span>
      <span class="s2" role="img" aria-label="Bookmarking profile"></span>
      <span class="s3" role="img" aria-label="Social network profile"></span>
      <span class="s4" role="img" aria-label="Microblog profile"></span>
      <span class="s5" role="img" aria-label="Video channel"></span>
      <span class="s6" role="img" aria-label="Discovery profile"></span>
    </div>
  </div>

  <h3 class="abs work-title">WORK WITH US</h3>
  <div class="abs work-card" role="img" aria-label="Photo of glasses resting on an employment application"></div>
  <a class="abs btn-red work-submit" href="#">Submit</a>
</aside>

<main>
  <article class="abs column col-prices">
    <h2>Our Prices</h2>
    <p><b>Lorem ipsum dolor sit amet, consectetur</b> adipiscing elit. Duis ligula est, viverra ut pretium quis, dignissim at purus. Proin neque est, fringilla quis rutrum at, pulvinar auctor nisl.</p>
    <p><b>Sed gravida ultricies ligula quis luctus.</b> Nullam ullamcorper, tellus nec cursus aliquet, nunc sapien pretium mi, id faucibus lacus orci a erat. Nunc laoreet turpis et magna congue sed bibendum sem mattis. Sed rutrum, elit quis laoreet auctor, sapien elit condimentum orci, eu eleifend sem odio vel nisl. Curabitur nunc mauris, pellentesque ut imperdiet eget, molestie id nulla. Donec pulvinar semper pretium. Integer sodales auctor est, eu pulvinar orci malesuada eget. Aenean</p>
    <a class="read-more" href="#">Read more</a>
  </article>

  <article class="abs column col-work">
    <h2>Work With Us</h2>
    <p><b>Lorem ipsum dolor sit amet, consectetur</b> adipiscing elit. Duis ligula est, viverra ut pretium quis, dignissim at purus. Proin neque est, fringilla quis rutrum at, pulvinar auctor nisl. Sed gravida ultricies ligula quis luctus. Nullam ullamcorper</p>
    <p><b>Tellus nec cursus aliquet, nunc</b> sapien pretium mi, id faucibus lacus orci a erat. Nunc laoreet turpis et magna congue sed bibendum sem mattis. Sed rutrum, elit quis laoreet auctor, sapien elit condimentum orci, eu eleifend sem odio vel nisl. Curabitur nunc mauris, pellentesque ut imperdiet eget, molestie id nulla. Donec pulvinar semper pretium. Integer sodales auctor est, eu pulvinar orci malesuada eget.</p>
    <a class="read-more" href="#">Read more</a>
  </article>
</main>

<footer class="abs footer">
  <div class="abs footer-brand">
    <span class="brand-name">quillpage<br>words.com</span>
  </div>
  <div class="abs footer-legal">© 2010 &nbsp;|&nbsp; Privacy Policy</div>
  <nav class="abs footer-nav">
    <a href="#">Home</a><a href="#">About Us</a><a href="#">Services</a><a href="#">Samples</a><a href="#">Pricing</a><a href="#">Clients</a><a href="#">Carrer</a><a href="#">Contact US</a>
  </nav>
</footer>

</body>
</html>
```